Something clear, simple easy to read, not to busy, gets straight to the point.

Keystone Lane Property Management specializes in single family homes. We offer property owners full Real Estate residential services. We provide the highest quality management service using state-of-the-art technology to keep them informed of how their investments are doing in real time, while providing tenants of these properties real time access to maintenance requests and billing.
Residential management includes but not limited to;
*tenant screening
*leasing
*monthly rent collection,
*property maintenance coordination
*financial reporting

Give us a call at (916) 555-0147 to see how we can work for you.

Save this card just in case.

Please add address and name on Back.
Martin Delacroix
Keystone Lane Property Management & Services
4715 Orlen Rd. C184,
Sacramento CA. 95899
Cell 916-555-0147
www.KeystoneLane.biz
BRE#04392758

Target Market(s)

Investors, property owners, Sacramento CA. USA

Industry/Entity Type

Property Management

Requirements
Must have
• Logo
Should not have
• not to busy.

```html
<!DOCTYPE html>
<html lang="en">
<head>
<meta charset="utf-8">
<title>Keystone Lane Property Management – Postcard</title>
<link rel="stylesheet" href="https://fonts.googleapis.com/css2?family=Cinzel:wght@400;700&family=Lato:wght@400;700&display=swap">
<style>
  :root{
    --brand-red:#9d0f17;
    --deep-red:#4a1212;
    --ink:#111111;
    --paper:#ffffff;
    --stage:#e6e6e6;
    --muted:#444444;
    --soft-pink:#f6dede;
    --stamp:#bcbcbc;
    --rule:#c8c8c8;
  }
  *{margin:0;padding:0;box-sizing:border-box}
  html,body{width:1200px;height:1200px;overflow:hidden;background:var(--stage)}
  .card{position:absolute;left:272px;width:694px;height:534px;background:var(--paper);
        overflow:hidden;box-shadow:3px 4px 8px rgba(0,0,0,.25)}
  .card--front{top:46px}
  .card--back{top:628px}
  .card__art{position:absolute;inset:0;width:694px;height:534px}
  .abs{position:absolute}
  .serif{font-family:"Cinzel",serif}
  .sans{font-family:"Lato",sans-serif}

  /* front */
  .brand-name{left:28px;top:80px;font-size:25px;color:var(--brand-red);font-family:"Cinzel",serif;font-weight:400;white-space:nowrap}
  .call{right:248px;top:30px;text-align:right;font-family:"Lato",sans-serif;color:var(--brand-red)}
  .call__lead{font-size:13px;line-height:16px}
  .call__phone{font-family:"Cinzel",serif;font-size:20px;color:var(--ink);line-height:26px;letter-spacing:.5px}
  .call__tail{font-size:12px;line-height:14px}
  .hero-title{left:24px;top:156px;font-size:33px;color:var(--paper);white-space:nowrap;font-family:"Cinzel",serif}
  .hero-rule{height:2px;background:var(--paper)}
  .hero-chip{left:25px;top:210px;width:189px;height:36px;background:var(--ink);color:var(--paper);
             font-family:"Cinzel",serif;font-size:30px;line-height:36px;padding-left:6px}
  .hero-sub{left:22px;top:258px;font-family:"Cinzel",serif;font-size:16px;line-height:20px;color:var(--soft-pink);letter-spacing:.6px}
  .hero-copy{left:22px;top:303px;font-family:"Lato",sans-serif;font-size:12.3px;line-height:16px;color:var(--paper)}
  .services-lead{left:26px;top:420px;font-family:"Lato",sans-serif;font-size:13.5px;color:var(--muted)}
  .services{font-family:"Lato",sans-serif;font-size:12.5px;line-height:17.5px;color:var(--muted);list-style:none}
  .services li{padding-left:15px;position:relative}
  .services li::before{content:"";position:absolute;left:2px;top:7px;width:4px;height:4px;border-radius:50%;background:var(--brand-red)}
  .web-strip{left:0;width:505px;top:513px;text-align:center;font-family:"Lato",sans-serif;font-weight:700;
             font-size:13px;letter-spacing:3px;color:var(--paper)}

  /* back */
  .save{left:0;width:240px;top:22px;text-align:center;font-family:"Cinzel",serif;font-weight:700;font-size:66px;line-height:66px;color:var(--brand-red)}
  .save-note{left:17px;top:97px;font-family:"Cinzel",serif;font-size:17px;color:var(--deep-red);letter-spacing:.4px}
  .back-title{left:20px;top:140px;font-family:"Cinzel",serif;font-size:33px;color:var(--paper);white-space:nowrap}
  .back-sub{left:18px;top:186px;font-family:"Cinzel",serif;font-size:19px;color:var(--deep-red);white-space:nowrap}
  .back-amp{left:19px;top:210px;font-family:"Cinzel",serif;font-size:34px;color:var(--paper);white-space:nowrap}
  .contact{left:22px;top:270px;list-style:none;font-family:"Lato",sans-serif;font-size:17px;color:var(--paper)}
  .contact li{display:flex;align-items:flex-start;gap:14px;line-height:21px;margin-bottom:9px}
  .contact svg{flex:0 0 16px;width:16px;height:16px;margin-top:2px}
  .name-bar{left:0;top:428px;width:290px;height:56px;background:var(--ink)}
  .name-bar__text{position:absolute;left:20px;top:12px;font-family:"Lato",sans-serif;font-weight:700;font-size:27px;color:var(--paper);white-space:nowrap}
  .portrait{left:206px;top:324px;width:254px;height:210px}
  .back-brand{left:330px;top:68px;width:152px;text-align:center;font-family:"Cinzel",serif;font-size:15px;color:var(--brand-red);white-space:nowrap}
  .stamp{left:598px;top:32px;width:62px;height:60px;background:var(--stamp)}
  .address-line{left:428px;width:236px;height:2px;background:var(--rule)}
</style>
</head>
<body>

<!-- FRONT -->
<section class="card card--front">
  <svg class="card__art" viewBox="0 0 694 534" aria-hidden="false">
    <defs>
      <linearGradient id="homeScene" x1="0" y1="0" x2="0" y2="1">
        <stop offset="0" stop-color="#b9d3ec"/>
        <stop offset=".3" stop-color="#eef1f3"/>
        <stop offset=".62" stop-color="#dcdfe1"/>
        <stop offset=".78" stop-color="#6f9a3d"/>
        <stop offset="1" stop-color="#7ea83f"/>
      </linearGradient>
      <linearGradient id="fadeLight" x1="0" y1="0" x2="1" y2="0">
        <stop offset="0" stop-color="#ffffff"/>
        <stop offset="1" stop-color="#ececec"/>
      </linearGradient>
    </defs>
    <rect x="0" y="0" width="694" height="534" fill="#ffffff"/>
    <polygon points="0,406 435,406 505,511 0,511" fill="url(#fadeLight)"/>
    <polygon points="0,146 426,146 342,266 435,406 0,406" fill="var(--brand-red)"/>
    <polygon points="0,511 505,511 520,534 0,534" fill="var(--brand-red)"/>
    <polygon role="img" aria-label="Photo of a white single family home with a front porch and green lawn"
             points="556,0 694,0 694,534 544,534 360,266" fill="url(#homeScene)"/>
    <polygon points="528,0 556,0 360,266 544,534 520,534 342,266" fill="var(--ink)"/>
    <polygon points="446,82 470,26 510,26 486,82" fill="var(--ink)"/>
  </svg>

  <div class="abs brand-name">Keystone Lane</div>

  <div class="abs call">
    <div class="call__lead">Give us a call at</div>
    <div class="call__phone">(916) 555-0147</div>
    <div class="call__tail">to see how we can work for you</div>
  </div>

  <h1 class="abs hero-title">Keystone Lane</h1>
  <div class="abs hero-rule" style="left:48px;top:203px;width:106px"></div>
  <div class="abs hero-chip">Property</div>
  <div class="abs hero-rule" style="left:30px;top:251px;width:184px"></div>

  <p class="abs hero-sub">Management specializes in<br>single family homes.</p>

  <p class="abs hero-copy">We offer property owners full Real Estate residential ser-<br>vices. We provide the highest quality management service<br>using state-of-the-art technology to keep them informed of<br>how their investments are doing in real time, while providing<br>tenants of these properties real time access to maintenance re-<br>quests and billing.</p>

  <p class="abs services-lead">Residential management includes but not limited to:</p>
  <ul class="abs services" style="left:26px;top:443px">
    <li>Tenant Screening</li>
    <li>Leasing</li>
    <li>Financial reporting</li>
  </ul>
  <ul class="abs services" style="left:174px;top:444px">
    <li>Monthly rent collection</li>
    <li>Property maintenance<br>coordination</li>
  </ul>

  <div class="abs web-strip">www.keystonelane.biz</div>
</section>

<!-- BACK -->
<section class="card card--back">
  <svg class="card__art" viewBox="0 0 694 534">
    <rect x="0" y="0" width="694" height="534" fill="#ffffff"/>
    <polygon points="0,0 206,0 398,260 340,345 340,534 0,534" fill="var(--brand-red)"/>
    <polygon points="0,26 225,26 268,84 0,84" fill="#ffffff"/>
    <polygon points="206,0 220,0 414,260 354,348 340,345 398,260" fill="var(--ink)"/>
  </svg>

  <div class="abs save">Save</div>
  <div class="abs save-note">This card just in case</div>

  <h2 class="abs back-title">Keystone Lane</h2>
  <div class="abs back-sub">Property Management</div>
  <div class="abs back-amp">&amp; Services</div>

  <ul class="abs contact">
    <li>
      <svg viewBox="0 0 16 16"><path d="M3.5 1.5l2.5 0 1 3.5-1.7 1.2a9 9 0 0 0 4.5 4.5l1.2-1.7 3.5 1v2.5c0 .8-.7 1.5-1.5 1.5A12 12 0 0 1 2 3c0-.8.7-1.5 1.5-1.5z" fill="none" stroke="#fff" stroke-width="1.5"/></svg>
      <span>916-555-0147</span>
    </li>
    <li>
      <svg viewBox="0 0 16 16"><circle cx="8" cy="8" r="6.5" fill="none" stroke="#fff" stroke-width="1.5"/><path d="M1.5 8h13M8 1.5c-3 3.5-3 9.5 0 13M8 1.5c3 3.5 3 9.5 0 13" fill="none" stroke="#fff" stroke-width="1.2"/></svg>
      <span>www.keystonelane.biz</span>
    </li>
    <li>
      <svg viewBox="0 0 16 16"><path d="M1.5 8L8 1.8 14.5 8M3.5 6.5V14.5h9V6.5" fill="none" stroke="#fff" stroke-width="1.5" stroke-linejoin="round"/></svg>
      <span>BRE#04392758</span>
    </li>
    <li>
      <svg viewBox="0 0 16 16"><path d="M8 15s-5-5.5-5-9a5 5 0 0 1 10 0c0 3.5-5 9-5 9z" fill="#fff"/><circle cx="8" cy="6" r="1.8" fill="var(--brand-red)"/></svg>
      <span>4715 Orlen Rd. C184,<br>Sacramento CA. 95899</span>
    </li>
  </ul>

  <div class="abs name-bar"><span class="name-bar__text">Martin Delacroix</span></div>

  <svg class="abs portrait" viewBox="0 0 254 210" role="img" aria-label="Portrait photo of Martin Delacroix in a dark suit and red tie">
    <defs>
      <linearGradient id="portraitTone" x1="0" y1="0" x2="0" y2="1">
        <stop offset="0" stop-color="#8a5a44"/>
        <stop offset=".55" stop-color="#3a2a28"/>
        <stop offset="1" stop-color="#161616"/>
      </linearGradient>
    </defs>
    <path d="M0 210 C10 150 60 130 90 118 L90 40 C90 10 170 10 170 40 L170 118 C205 132 240 150 254 210 Z" fill="url(#portraitTone)"/>
  </svg>

  <div class="abs back-brand">Keystone Lane</div>
  <div class="abs stamp"></div>
  <div class="abs address-line" style="top:152px"></div>
  <div class="abs address-line" style="top:182px"></div>
  <div class="abs address-line" style="top:211px"></div>
  <div class="abs address-line" style="top:240px"></div>
</section>

</body>
</html>
```